Logo for a gospel Ministry
Logo for a gospel ministry
Project: Logo for a gospel Ministry
Professional
Neema Tuvako & Halida Ruth Sesiwa
Harvesters
P.O Box 27350 Arusha Tanzania
neemahalida42@postmeadow.example

```html
<!DOCTYPE html>
<html lang="en">
<head>
<meta charset="utf-8">
<title>Kindled Hall Ministry — Business Card</title>
<link rel="stylesheet" href="https://fonts.googleapis.com/css2?family=Montserrat:wght@300;400;600&display=swap">
<style>
  :root {
    --page-bg: #ececec;
    --card-bg: #ffffff;
    --brand-blue: #1f3f95;
    --brand-red: #e8235a;
    --text-grey: #6b6b6b;
  }
  * { box-sizing: border-box; margin: 0; padding: 0; }
  html, body {
    width: 1200px;
    height: 1045px;
    overflow: hidden;
    background: var(--page-bg);
    font-family: "Montserrat", Arial, sans-serif;
  }
  .business-card {
    position: absolute;
    left: 75px;
    top: 222px;
    width: 1050px;
    height: 600px;
    background: var(--card-bg);
    overflow: hidden;
    box-shadow: 0 6px 18px rgba(0,0,0,0.18);
  }
  .card-swoosh {
    position: absolute;
    inset: 0;
    width: 100%;
    height: 100%;
  }
  .ministry-mark {
    position: absolute;
    left: 40px;
    top: 90px;
    display: flex;
    align-items: center;
    gap: 16px;
  }
  .ministry-mark__dot {
    width: 46px;
    height: 46px;
    border-radius: 50%;
    background: var(--brand-blue);
  }
  .ministry-mark__name {
    font-weight: 600;
    font-size: 30px;
    line-height: 1.1;
    color: var(--brand-blue);
  }
  .leaders {
    position: absolute;
    right: 254px;
    top: 126px;
    text-align: right;
  }
  .leaders__names {
    font-weight: 400;
    font-size: 28px;
    color: var(--brand-blue);
    white-space: nowrap;
  }
  .leaders__role {
    margin-top: 8px;
    font-weight: 300;
    font-size: 20px;
    color: var(--text-grey);
  }
  .contact {
    position: absolute;
    left: 67px;
    top: 276px;
    font-weight: 300;
    font-size: 20px;
    color: var(--text-grey);
    list-style: none;
  }
  .contact__address { margin-bottom: 22px; }
  .contact__item {
    display: flex;
    align-items: center;
    gap: 14px;
    height: 38px;
  }
  .contact__icon { width: 18px; height: 18px; flex: none; }
</style>
</head>
<body>
  <article class="business-card">
    <svg class="card-swoosh" viewBox="0 0 1050 600" preserveAspectRatio="none" aria-hidden="true">
      <path fill="var(--brand-red)" d="M735,0 C930,70 950,340 400,600 L610,600 C900,470 990,230 790,0 Z"/>
      <path fill="var(--brand-blue)" d="M790,0 L1050,0 L1050,600 L610,600 C900,470 990,230 790,0 Z"/>
    </svg>

    <div class="ministry-mark">
      <span class="ministry-mark__dot"></span>
      <span class="ministry-mark__name">Kindled Hall<br>Ministry</span>
    </div>

    <div class="leaders">
      <p class="leaders__names">Neema Tuvako &amp; Halida Ruth Sesiwa</p>
      <p class="leaders__role">Harvesters</p>
    </div>

    <ul class="contact">
      <li class="contact__address">P.O Box 27350 Arusha Tanzania</li>
      <li class="contact__item">
        <svg class="contact__icon" viewBox="0 0 24 24" aria-hidden="true">
          <path fill="var(--brand-red)" d="M6.6 10.8a15 15 0 0 0 6.6 6.6l2.2-2.2c.3-.3.7-.4 1-.2 1.1.4 2.3.6 3.6.6.6 0 1 .4 1 1V20c0 .6-.4 1-1 1A17 17 0 0 1 3 4c0-.6.4-1 1-1h3.5c.6 0 1 .4 1 1 0 1.3.2 2.5.6 3.6.1.3 0 .7-.2 1z"/>
        </svg>
        <span>+255710382654</span>
      </li>
      <li class="contact__item">
        <svg class="contact__icon" viewBox="0 0 24 24" aria-hidden="true">
          <rect x="6" y="2" width="12" height="20" rx="2" fill="none" stroke="var(--brand-red)" stroke-width="2.4"/>
          <circle cx="12" cy="18" r="1.3" fill="var(--brand-red)"/>
        </svg>
        <span>+255689174203</span>
      </li>
      <li class="contact__item">
        <svg class="contact__icon" viewBox="0 0 24 24" aria-hidden="true">
          <rect x="2" y="5" width="20" height="14" rx="1.5" fill="var(--brand-red)"/>
          <path d="M3 6.5l9 6.5 9-6.5" fill="none" stroke="#fff" stroke-width="1.6"/>
        </svg>
        <span>neemahalida42@postmeadow.example</span>
      </li>
    </ul>
  </article>
</body>
</html>
```